Tattoo Shop Business Card

I need a Business Card for the The Harbor Quill.

I'm thinking i want a double sided business card, really clean, very classy, one side the logo, and on the other my information. I'm pretty much open to anything, as long as its fun and captures class and elegance, while at the same time is edgy and tattooish.
I don't want your typical classic card. Add your own twist on it

Logo is attached to this brief

Please include:
Name
Position
Phone Number
Email
Website

Target Market(s)

I'm looking to capture potential clients for my tattoo shop so the card needs to be something they can fit in their wallet but they will also remember me when they see that card in there. My target audience is everyone over 18 that is intrigued by tattoos and piercings.

Industry/Entity Type

Business

Font styles to use
Serif

Colors

Designer to choose colors to be used in the design.

Requirements
Must have
• must be bold and something people will never forget

```html
<!DOCTYPE html>
<html lang="en">
<head>
<meta charset="utf-8">
<title>The Harbor Quill – Business Card</title>
<link href="https://fonts.googleapis.com/css2?family=Libre+Baskerville:wght@400;700&display=swap" rel="stylesheet">
<style>
  :root {
    --backdrop: #f1f0ed;
    --card-dark: #0e0705;
    --card-glow: #4a230f;
    --card-mid: #24120a;
    --grain-warm: rgba(150, 70, 25, 0.10);
    --grain-dark: rgba(0, 0, 0, 0.18);
    --brand-gold: #dba640;
    --brand-red: #8c1a12;
    --ornament-gold: rgba(219, 166, 64, 0.55);
    --ornament-white: rgba(244, 241, 234, 0.55);
    --ink-white: #f4f1ea;
  }
  * { margin: 0; padding: 0; box-sizing: border-box; }
  html, body {
    width: 900px;
    height: 1200px;
    overflow: hidden;
    background: var(--backdrop);
  }
  body {
    position: relative;
    font-family: "Libre Baskerville", "Times New Roman", serif;
  }
  .card {
    position: absolute;
    left: 30px;
    width: 842px;
    height: 482px;
    overflow: hidden;
    color: var(--ink-white);
    text-align: center;
    background:
      repeating-linear-gradient(87deg, var(--grain-warm) 0 1px, transparent 1px 4px),
      repeating-linear-gradient(3deg, var(--grain-dark) 0 1px, transparent 1px 5px),
      radial-gradient(ellipse 70% 60% at 30% 35%, rgba(90, 40, 15, 0.35), transparent 70%),
      radial-gradient(ellipse 60% 55% at 72% 62%, rgba(80, 30, 12, 0.35), transparent 70%),
      radial-gradient(ellipse at 50% 45%, var(--card-glow) 0%, var(--card-mid) 50%, var(--card-dark) 100%);
  }
  .card--front { top: 108px; }
  .card--back  { top: 610px; }

  .brand-name {
    position: absolute;
    left: 0;
    right: 0;
    font-weight: 700;
    text-transform: uppercase;
    line-height: 1;
    white-space: nowrap;
  }
  .card--front .brand-name {
    top: 212px;
    font-size: 52px;
    letter-spacing: 1px;
    color: var(--brand-gold);
  }
  .card--back .brand-name {
    top: 124px;
    font-size: 38px;
    letter-spacing: 1px;
    color: var(--ink-white);
  }

  .ornament-row {
    position: absolute;
    left: 0;
    right: 0;
    display: flex;
    justify-content: center;
    align-items: center;
  }
  .card--front .ornament-row { top: 318px; gap: 18px; }
  .card--back .ornament-row { top: 196px; gap: 14px; }
  .ornament {
    border-radius: 12px;
  }
  .card--front .ornament {
    width: 130px;
    height: 26px;
    background: radial-gradient(ellipse at center, var(--ornament-gold), transparent 72%);
  }
  .card--back .ornament {
    width: 96px;
    height: 20px;
    background: radial-gradient(ellipse at center, var(--ornament-white), transparent 72%);
  }
  .place-band {
    font-weight: 700;
    text-transform: uppercase;
    letter-spacing: 3px;
    line-height: 1;
  }
  .card--front .place-band {
    padding: 6px 18px;
    font-size: 17px;
    color: var(--brand-gold);
    background: var(--brand-red);
  }
  .card--back .place-band {
    padding: 4px 14px;
    font-size: 13px;
    color: var(--card-dark);
    background: var(--ink-white);
  }

  .contact {
    position: absolute;
    left: 0;
    right: 0;
    top: 278px;
    line-height: 1;
  }
  .contact__name {
    font-size: 33px;
    letter-spacing: 1px;
  }
  .contact__role {
    margin-top: 8px;
    font-size: 17px;
    letter-spacing: 1px;
  }
  .contact__phone {
    margin-top: 32px;
    font-size: 19px;
  }
  .contact__links {
    margin-top: 9px;
    font-size: 19px;
  }
  .contact__links span + span { margin-left: 28px; }
</style>
</head>
<body>
  <section class="card card--front" aria-label="Card front">
    <h1 class="brand-name">The Harbor Quill</h1>
    <div class="ornament-row">
      <div class="ornament" role="img" aria-label="Gold scroll flourish"></div>
      <span class="place-band">Saltmarsh</span>
      <div class="ornament" role="img" aria-label="Gold scroll flourish"></div>
    </div>
  </section>

  <section class="card card--back" aria-label="Card back">
    <p class="brand-name">The Harbor Quill</p>
    <div class="ornament-row">
      <div class="ornament" role="img" aria-label="White scroll flourish"></div>
      <span class="place-band">Saltmarsh</span>
      <div class="ornament" role="img" aria-label="White scroll flourish"></div>
    </div>
    <div class="contact">
      <p class="contact__name">HARBOR QUILL</p>
      <p class="contact__role">TATTOO ARTIST</p>
      <p class="contact__phone">0000000000 / 00000000</p>
      <p class="contact__links"><span>email@inkmail.com</span><span>www.website.com</span></p>
    </div>
  </section>
</body>
</html>
```